Ferrowave.com website design

I need a basic website for www.ferrowave.com. Ferro Wave has been hosting websites since 2002 via partnership arrangement with Stackhollow.com and Namequarry.com. We do not do any design, only hosting for small companies and nonprofits. We are referring people to PixelGuild and others to get their websites developed. Our website and pricing does not change often, but I need to be able to easily update the pricing and contact page.

Target Market(s)

Small company and non profit organizations

Industry/Entity Type

Utility

Coding

Coded - Design and coding required

Number of Pages Required

5+ page

Colors

Designer to choose colors to be used in the design.

Requirements
Must have
• Wordsmith format for easy content management. The logo attached. Contact us page with the following: Phone and fax are the same number: 888.514.2973. Email address is myferrowave@mailnest.example. Mailing address is 4819 E. Tolliver Bend #317, Coldridge, AR 72950.
Nice to have
• Some kind of badge or tag line on the home page that celebrates our 15th year of hosting without a single hosting without any downtime. We are are 15 year partners with Stackhollow.com and Namequarry.com. Website Design tab needs to reference PixelGuild or others for all their website design needs. We provide no design or updating services. We will provide the developers FTP access to our dedicated Linux server. We do not provide email services other than redirects to their proprietary email or gmail, yahoo, etc. Needs a services and pricing tab. We provide domain registration services via our partnership with Namequarry.com. We will want a way for them to submit a suggested domain name for us to verify if available. I might be able to get a link from Namequarry.com to our account for you to include on that tab REGISTER DOMAIN. The tab buttons can be: WHO WE ARE, WHAT WE DO, WHEN YOU NEED US, WHERE TO REACH US. Maybe consider making the WHO, WHAT, WHEN and WHERE a dark blue color the rest of the text different color just so they stand out
Should not have
• A lot of animation that takes a long time to open. Clean and simple website.

```html
<!DOCTYPE html>
<html lang="en">
<head>
<meta charset="utf-8">
<title>Ferro Wave – Website Hosting</title>
<link rel="stylesheet" href="https://fonts.googleapis.com/css2?family=Lato:wght@400;700;900&family=Open+Sans:wght@400;600&family=Oswald:wght@400;500&family=Roboto:wght@400;500&display=swap">
<style>
:root{
  --blue:#5aaeea;
  --navy:#0a4a7f;
  --ink:#2b2b2b;
  --pale:#f3f7fb;
  --grey:#ececec;
  --footer:#2d2d2d;
  --footer-deep:#1e1e1e;
  --white:#fff;
}
*{margin:0;padding:0;box-sizing:border-box}
html,body{width:1200px;height:3448px;overflow:hidden}
body{position:relative;background:var(--white);font-family:"Open Sans",Arial,sans-serif;color:var(--ink)}
.abs{position:absolute}
.center{left:0;width:1200px;text-align:center}

/* header */
.site-header{position:absolute;left:0;top:0;width:1200px;height:150px;background:var(--white);z-index:3}
.brand-plate{position:absolute;left:97px;top:0;width:225px;height:212px;z-index:4}
.brand{position:absolute;left:97px;top:100px;width:225px;display:flex;align-items:center;justify-content:center;gap:10px;z-index:5;
  font-family:"Lato",sans-serif;font-weight:900;font-size:25px;color:var(--navy);letter-spacing:.5px;white-space:nowrap}
.brand-square{width:22px;height:22px;background:var(--navy)}
.top-contacts{position:absolute;right:62px;top:26px;display:flex;gap:26px;font-family:"Roboto",sans-serif;font-size:17px;white-space:nowrap}
.top-contacts span{display:flex;align-items:center;gap:10px}
.top-contacts .phone{color:var(--blue)}
.top-contacts .mail{color:var(--navy)}
.top-contacts svg{width:32px;height:32px}
.main-nav a{position:absolute;top:108px;font-family:"Roboto",sans-serif;font-size:15px;color:#222;text-decoration:none;white-space:nowrap}
.main-nav a.active{color:var(--blue);border-bottom:2px solid var(--blue);padding:0 14px 12px}
.nav-mark{position:absolute;left:452px;top:78px;width:20px;height:20px;border:2px solid #cfe2f2}

/* hero */
.hero{position:absolute;left:0;top:150px;width:1200px;height:560px}
.hero-photo{position:absolute;inset:0;clip-path:polygon(0 0,100% 0,100% 505px,50% 540px,0 505px);
  background:linear-gradient(120deg,#3b4048 0%,#6c727a 40%,#8b9199 62%,#4c5259 100%)}
.hero-title{top:140px;font-family:"Lato",sans-serif;font-weight:900;font-size:72px;color:var(--white);letter-spacing:3px;white-space:nowrap}
.hero-quote{top:255px;font-family:"Roboto",sans-serif;font-weight:500;font-size:27px;line-height:50px;color:var(--white)}
.hero-dots{position:absolute;left:558px;top:507px;display:flex;gap:6px}
.hero-dots i{width:12px;height:12px;border-radius:50%;background:var(--white)}
.hero-dots i:first-child{background:var(--blue)}

/* welcome */
.kicker{top:810px;font-family:"Lato",sans-serif;font-size:24px;color:var(--blue);letter-spacing:1px}
.welcome-name{top:852px;font-family:"Lato",sans-serif;font-weight:900;font-size:46px;color:var(--navy);letter-spacing:1px;white-space:nowrap}
.rule{position:absolute;height:2px;width:120px;background:var(--navy)}
.lead{position:absolute;left:130px;width:940px;text-align:center;font-size:13.5px;line-height:25px;color:#444}
.btn{position:absolute;height:46px;display:flex;align-items:center;justify-content:center;font-size:14px;font-weight:600;text-decoration:none;white-space:nowrap}
.btn-solid{background:var(--blue);color:var(--white)}
.btn-outline{background:var(--white);color:var(--navy);border:2px solid var(--navy)}

/* services */
.services{position:absolute;left:0;top:1225px;width:1200px;height:511px}
.service{position:absolute;top:0;width:600px;height:511px;text-align:center;color:var(--white)}
.service h2{position:absolute;top:195px;width:100%;font-family:"Lato",sans-serif;font-weight:400;font-size:32px;letter-spacing:.5px;white-space:nowrap}
.service h2 b{font-weight:900}
.service p{position:absolute;left:55px;top:264px;width:490px;font-size:13px;line-height:25px}
.service .btn{top:376px;left:245px;width:110px}
.service svg.icon{position:absolute;left:265px;top:96px;width:70px;height:70px}

/* what we do */
.section-title{font-family:"Lato",sans-serif;font-weight:900;font-size:32px;color:var(--navy);white-space:nowrap}
.feature{position:absolute;width:480px;height:90px}
.feature .disc{position:absolute;left:0;top:0;width:84px;height:84px;border-radius:50%;display:flex;align-items:center;justify-content:center}
.feature .disc svg{width:44px;height:44px}
.feature h3{position:absolute;left:100px;top:6px;font-family:"Roboto",sans-serif;font-weight:500;font-size:18px;letter-spacing:.3px;white-space:nowrap}
.feature p{position:absolute;left:100px;top:36px;width:375px;font-size:13px;line-height:24px;color:#444}
.light-c{background:var(--blue)} .navy-c{background:var(--navy)}
.t-light{color:var(--blue)} .t-navy{color:var(--navy)}

/* packages */
.packages{position:absolute;left:0;top:2253px;width:1200px;height:747px;background:var(--pale)}
.tabs{position:absolute;left:99px;top:170px;display:flex}
.tab{width:334px;height:69px;display:flex;align-items:center;justify-content:center;background:var(--grey);
  font-family:"Lato",sans-serif;font-weight:700;font-size:23px;color:#222;position:relative;white-space:nowrap}
.tab.active{background:var(--blue);color:var(--white)}
.tab.active::after{content:"";position:absolute;left:152px;top:69px;border:15px solid transparent;border-top-color:var(--blue)}
.plan{position:absolute;text-align:center}
.plan h3{font-family:"Roboto",sans-serif;font-weight:400;font-size:26px}
.plan .from{font-size:15px;margin-top:12px}
.plan .price{font-family:"Oswald",sans-serif;font-weight:500;font-size:39px;margin-top:14px}
.plan .desc{font-size:14px;line-height:26px;margin:10px auto 0;width:150px}
.plan .order{display:inline-block;margin-top:16px;width:120px;height:36px;line-height:32px;border:2px solid #333;border-radius:18px;
  font-family:"Oswald",sans-serif;font-size:13px;color:#222;text-decoration:none}
.plan.side{background:var(--grey);width:222px;height:301px;top:338px;padding-top:37px;color:#222}
.plan.side .price{color:var(--blue)}
.plan.featured{left:439px;top:308px;width:322px;height:363px;background:var(--blue);color:var(--white);box-shadow:0 4px 14px rgba(0,0,0,.25);padding-top:106px}
.plan.featured .from{color:#e5f2fc}
.plan.featured .order{border-color:var(--white);color:var(--white)}
.badge{position:absolute;left:90px;top:28px;width:142px;height:46px;background:var(--white);color:var(--blue);
  font-family:"Roboto",sans-serif;font-size:21px;line-height:46px;letter-spacing:.5px}

/* footer */
.site-footer{position:absolute;left:0;top:3000px;width:1200px;height:384px;background:var(--footer);color:var(--white)}
.site-footer h4{position:absolute;top:72px;font-family:"Lato",sans-serif;font-weight:700;font-size:20px;letter-spacing:.3px;white-space:nowrap}
.site-footer .rule{top:115px;width:70px;background:var(--blue)}
.about-text{position:absolute;left:99px;top:138px;width:432px;font-size:13px;line-height:21px;color:#e0e0e0;text-align:justify}
.more{position:absolute;left:99px;top:264px;font-size:15px;color:var(--blue);text-decoration:none}
.links{position:absolute;left:607px;top:138px;list-style:none;font-size:15px;color:#eee;white-space:nowrap}
.links li{height:41.5px;display:flex;align-items:flex-start;gap:14px}
.links li::before{content:"›";font-size:18px;line-height:20px}
.pill{position:absolute;left:835px;background:var(--blue);border-radius:23px;display:flex;align-items:center;gap:10px;padding:0 22px;
  font-family:"Roboto",sans-serif;font-size:15px;color:var(--white);white-space:nowrap}
.pill svg{width:16px;height:16px;flex:none}
.copyright{position:absolute;left:0;top:3384px;width:1200px;height:64px;background:var(--footer-deep);color:#ddd;
  font-size:13px;text-align:center;line-height:64px}
</style>
</head>
<body>

<header class="site-header">
  <div class="top-contacts">
    <span class="phone"><svg viewBox="0 0 32 32"><circle cx="16" cy="16" r="16" fill="#5aaeea"/><path d="M11 9l3 0 1 4-2 1.5c1 2 2.5 3.5 4.5 4.5L19 17l4 1v3c0 1-1 2-2 2-6 0-12-6-12-12 0-1 1-2 2-2z" fill="#fff"/></svg>888.514.2973</span>
    <span class="mail"><svg viewBox="0 0 32 32"><circle cx="16" cy="16" r="16" fill="#0a4a7f"/><rect x="9" y="11" width="14" height="10" fill="none" stroke="#fff" stroke-width="1.8"/><path d="M9 11l7 6 7-6" fill="none" stroke="#fff" stroke-width="1.8"/></svg>myferrowave@mailnest.example</span>
  </div>
  <span class="nav-mark"></span>
  <nav class="main-nav">
    <a class="active" href="#" style="left:438px">Home</a>
    <a href="#" style="left:538px">Who we are</a>
    <a href="#" style="left:671px">What we do</a>
    <a href="#" style="left:805px">When you need us</a>
    <a href="#" style="left:981px">Where to reach us</a>
  </nav>
</header>

<svg class="brand-plate" viewBox="0 0 225 212"><path d="M3 0V148L112 208 222 148V0" fill="#fff" stroke="#0a4a7f" stroke-width="4"/></svg>
<div class="brand"><span class="brand-square"></span>FERRO WAVE</div>

<section class="hero">
  <div class="hero-photo" role="img" aria-label="Photo of two people working at computers in a bright office"></div>
  <svg class="abs" style="left:0;top:495px" width="1200" height="60" viewBox="0 0 1200 60"><path d="M0 12 600 47 1200 12" fill="none" stroke="#5aaeea" stroke-width="6"/></svg>
  <h1 class="abs center hero-title">FERRO WAVE</h1>
  <p class="abs center hero-quote">" 15th year of hosting without a single hosting<br>without any downtime "</p>
  <div class="hero-dots"><i></i><i></i><i></i><i></i><i></i></div>
</section>

<section class="welcome">
  <p class="abs center kicker">WELCOME</p>
  <h2 class="abs center welcome-name">FERRO WAVE</h2>
  <span class="rule" style="left:540px;top:925px"></span>
  <p class="lead" style="top:962px">Nemo enim ipsam voluptatem quia voluptas sit aspernatur aut odit aut fugit, sed quia consequuntur magni dolores eos qui ratione voluptatem sequi nesciunt. Neque porro quisquam est, qui dolorem ipsum quia dolor sit amet, consectetur, adipisci velit, sed quia non numquam eius modi tempora incidunt ut labore et dolore magnam aliquam quaerat voluptatem.</p>
  <p class="lead" style="top:1050px">Consectetur, adipisci velit, sed quia non numquam eius modi tempora incidunt ut labore et dolore magnam aliquam quaerat voluptatem.<br>Ut enim ad minima veniam, quis nostrum exercitationem.</p>
  <a class="btn btn-solid" href="#" style="left:478px;top:1138px;width:116px">Read More</a>
  <a class="btn btn-outline" href="#" style="left:607px;top:1138px;width:116px">Contact Us</a>
</section>

<section class="services">
  <svg class="abs" style="left:0;top:0" width="1200" height="511" viewBox="0 0 1200 511">
    <polygon points="0,0 600,53 600,465 0,511" fill="#5aaeea"/>
    <polygon points="600,53 1200,0 1200,511 600,465" fill="#0a4a7f"/>
  </svg>
  <div class="service" style="left:0">
    <svg class="icon" viewBox="0 0 70 70"><g fill="#fff"><rect x="6" y="4" width="58" height="14" rx="2"/><rect x="6" y="22" width="58" height="14" rx="2"/><rect x="6" y="40" width="58" height="14" rx="2"/><rect x="33" y="54" width="4" height="8"/><rect x="4" y="62" width="62" height="3"/></g><g fill="#5aaeea"><circle cx="14" cy="11" r="2"/><circle cx="14" cy="29" r="2"/><circle cx="14" cy="47" r="2"/></g></svg>
    <h2><b>WEBHOST</b> SERVICES</h2>
    <p>Sed ut perspiciatis unde omnis iste natus error sit voluptatem accusantium doloremque laudantium, totam rem aperiam, eaque ipsa quae ab illo inven tore veritatis et quasi architecto beatae vitae dicta sunt explicabo.</p>
    <a class="btn" href="#" style="background:#0a4a7f;color:#fff">Read More</a>
  </div>
  <div class="service" style="left:600px">
    <svg class="icon" viewBox="0 0 70 70"><path d="M16 4h28l12 12v50H16z" fill="#fff"/><path d="M44 4v12h12" fill="#ddd"/><rect x="8" y="36" width="46" height="16" fill="#0a4a7f"/><text x="31" y="48" font-family="Arial" font-size="11" font-weight="700" fill="#fff" text-anchor="middle">.COM</text></svg>
    <h2><b>DOMAIN</b> SERVICES</h2>
    <p>Sed ut perspiciatis unde omnis iste natus error sit voluptatem accusantium doloremque laudantium, totam rem aperiam, eaque ipsa quae ab illo inven tore veritatis et quasi architecto beatae vitae dicta sunt explicabo.</p>
    <a class="btn btn-solid" href="#">Read More</a>
  </div>
</section>

<section class="what-we-do">
  <h2 class="abs center section-title" style="top:1768px">WHAT WE DO</h2>
  <p class="lead" style="top:1826px">Nemo enim ipsam voluptatem quia voluptas sit aspernatur aut odit aut fugit, sed quia consequuntur magni dolores eos qui ratione voluptatem sequi nesciunt. Neque porro quisquam est, qui dolorem ipsum quia dolor.</p>

  <div class="feature" style="left:99px;top:1948px">
    <div class="disc light-c"><svg viewBox="0 0 44 44"><rect x="6" y="11" width="32" height="22" fill="none" stroke="#fff" stroke-width="2.5"/><path d="M6 11l16 13 16-13" fill="none" stroke="#fff" stroke-width="2.5"/></svg></div>
    <h3 class="t-light">YOUR VERY OWN E-MAIL</h3>
    <p>Nemo enim ipsam voluptatem quia voluptas sit asperna tur aut odit aut fugit, sed quia.</p>
  </div>
  <div class="feature" style="left:642px;top:1948px">
    <div class="disc navy-c"><svg viewBox="0 0 44 44"><rect x="6" y="6" width="32" height="32" rx="4" fill="none" stroke="#fff" stroke-width="2.5"/><text x="22" y="30" font-family="Arial" font-size="20" font-weight="700" fill="#fff" text-anchor="middle">@</text></svg></div>
    <h3 class="t-navy">UNLIMITED EVERYTHING</h3>
    <p>Nemo enim ipsam voluptatem quia voluptas sit asperna tur aut odit aut fugit, sed quia.</p>
  </div>
  <div class="feature" style="left:99px;top:2086px">
    <div class="disc navy-c"><svg viewBox="0 0 44 44"><circle cx="18" cy="13" r="6" fill="#fff"/><path d="M6 36c0-9 5-14 12-14s12 5 12 14z" fill="#fff"/><rect x="24" y="26" width="16" height="11" fill="#fff" stroke="#0a4a7f" stroke-width="2"/></svg></div>
    <h3 class="t-navy">A DEVELOPER'S DREAM</h3>
    <p>Nemo enim ipsam voluptatem quia voluptas sit asperna tur aut odit aut fugit, sed quia.</p>
  </div>
  <div class="feature" style="left:642px;top:2086px">
    <div class="disc light-c"><svg viewBox="0 0 44 44"><path d="M9 24a13 13 0 0 1 26 0" fill="none" stroke="#fff" stroke-width="3"/><rect x="6" y="22" width="7" height="11" rx="2" fill="#fff"/><rect x="31" y="22" width="7" height="11" rx="2" fill="#fff"/><circle cx="22" cy="26" r="6" fill="#fff"/></svg></div>
    <h3 class="t-light">TIRELESS SUPPORT</h3>
    <p>Nemo enim ipsam voluptatem quia voluptas sit asperna tur aut odit aut fugit, sed quia.</p>
  </div>
</section>

<section class="packages">
  <h2 class="abs center section-title" style="top:50px">OUR PACKAGES</h2>
  <span class="rule" style="left:540px;top:105px"></span>
  <div class="tabs">
    <div class="tab">SHARED HOSTING</div>
    <div class="tab active">VPS HOSTING</div>
    <div class="tab">DEDICATED HOSTING</div>
  </div>
  <div class="plan side" style="left:216px">
    <h3>Plan 1</h3><p class="from">Starting At</p><p class="price">$6.99</p>
    <p class="desc">Lorem ipsum dolor sit consectetur elit.</p><a class="order" href="#">ORDER NOW</a>
  </div>
  <div class="plan side" style="left:761px">
    <h3>Plan 3</h3><p class="from">Starting At</p><p class="price">$9.99</p>
    <p class="desc">Lorem ipsum dolor sit consectetur elit.</p><a class="order" href="#">ORDER NOW</a>
  </div>
  <div class="plan featured">
    <span class="badge">POPULAR</span>
    <h3>Plan 2</h3><p class="from">Starting At</p><p class="price">$7.99</p>
    <p class="desc">Lorem ipsum dolor sit consectetur elit.</p><a class="order" href="#">ORDER NOW</a>
  </div>
</section>

<footer class="site-footer">
  <h4 style="left:99px">ABOUT US</h4><span class="rule" style="left:99px"></span>
  <p class="about-text">Lorem ipsum dolor sit amet, consectetur adipisicing elit. Laborum quod mollit tia quisquam. Architecto quam in atque sint voluptatem, conseqa tur con sectetur ab ipsum maxime quod consequuntur excepturi illum dolorem ex modi.Lorem ipsum dolor sit amet, consectetur adipisicing elit. Consectetur animi id ex perspiciatis.</p>
  <a class="more" href="#">Read More &gt;</a>

  <h4 style="left:607px">USEFUL LINKS</h4><span class="rule" style="left:607px"></span>
  <ul class="links">
    <li>Home</li><li>Who we are</li><li>What we do</li><li>When you need us</li><li>Where to reach us</li>
  </ul>

  <h4 style="left:835px">CONTACT</h4><span class="rule" style="left:835px"></span>
  <div class="pill" style="top:149px;height:46px;width:222px"><svg viewBox="0 0 16 16"><path d="M3 1h3l1 4-2 1c1 2 2 3 4 4l1-2 4 1v3c0 1-1 2-2 2C6 14 2 10 2 3c0-1 0-2 1-2z" fill="#fff"/></svg>888.514.2973</div>
  <div class="pill" style="top:202px;height:46px;width:266px;font-size:13.5px;padding:0 14px"><svg viewBox="0 0 16 16"><rect x="1" y="3" width="14" height="10" fill="#fff"/><path d="M1 3l7 6 7-6" fill="none" stroke="#5aaeea" stroke-width="1.5"/></svg>myferrowave@mailnest.example</div>
  <div class="pill" style="top:267px;height:72px;width:266px;align-items:flex-start;padding-top:13px;line-height:23px;font-size:14.5px"><svg viewBox="0 0 16 16" style="margin-top:3px"><path d="M8 1a5 5 0 0 1 5 5c0 4-5 9-5 9S3 10 3 6a5 5 0 0 1 5-5z" fill="#fff"/><circle cx="8" cy="6" r="2" fill="#5aaeea"/></svg><span>4819 E. Tolliver Bend #317,<br>Coldridge, AR 72950</span></div>
</footer>
<p class="copyright">Copyright © 2017 Ferro Wave. All Rights Reserved.</p>

</body>
</html>
```